Tidewell Outdoor Signage

We need an outdoor signage design for my company with new logo designed from makerhive. We do electrical, Air conditioning & Plumbing, installation, service, repairs and maintenance. The design shall be an eye catching that cannot miss ready it.

Industry/Entity Type

Electrical, Air conditioning, Plumbing

```html
<!DOCTYPE html>
<html lang="en">
<head>
<meta charset="UTF-8">
<title>Tidewell Outdoor Signage</title>
<link rel="stylesheet" href="https://fonts.googleapis.com/css2?family=Poppins:wght@600;700&display=swap">
<style>
  :root {
    --brand-blue: #1763a8;
    --brand-red: #e82127;
    --brand-red-dark: #a8191f;
    --brand-orange: #ef8a3c;
    --brand-white: #ffffff;
    --page-bg: #eceeef;
  }
  html, body {
    margin: 0;
    padding: 0;
    width: 1200px;
    height: 1117px;
    overflow: hidden;
    background: var(--page-bg);
    font-family: "Poppins", sans-serif;
  }
  .sign-frame {
    position: absolute;
    left: 20px;
    top: 259px;
    width: 1160px;
    height: 598px;
    box-shadow: 0 10px 30px rgba(0,0,0,0.18);
    overflow: hidden;
  }
  .sign {
    position: absolute;
    left: 0;
    top: 0;
    width: 1570px;
    height: 810px;
    transform: scale(0.7389);
    transform-origin: 0 0;
    background: var(--brand-white);
  }
  .sign-art {
    position: absolute;
    inset: 0;
    width: 1570px;
    height: 810px;
  }
  .brand-name {
    position: absolute;
    left: 104px;
    top: 330px;
    margin: 0;
    font-weight: 600;
    font-size: 150px;
    line-height: 1;
    letter-spacing: -3px;
    color: var(--brand-orange);
  }
  .brand-tagline {
    position: absolute;
    left: 102px;
    top: 478px;
    margin: 0;
    font-weight: 600;
    font-size: 32px;
    line-height: 1;
    white-space: nowrap;
  }
  .brand-tagline span { margin-right: 18px; }
  .tag-electrical { color: var(--brand-red); }
  .tag-air { color: var(--brand-blue); }
  .tag-plumbing { color: var(--brand-orange); }
  .services-title {
    position: absolute;
    left: 960px;
    top: 96px;
    width: 560px;
    margin: 0;
    text-align: center;
    font-weight: 700;
    font-size: 84px;
    line-height: 120px;
    color: var(--brand-white);
    text-shadow: 3px 3px 4px rgba(0,0,0,0.35);
  }
  .services-list {
    position: absolute;
    left: 830px;
    top: 258px;
    width: 680px;
    margin: 0;
    text-align: center;
    font-weight: 600;
    font-size: 54px;
    line-height: 64px;
    color: var(--brand-white);
  }
  .website {
    position: absolute;
    left: 365px;
    top: 632px;
    width: 870px;
    margin: 0;
    text-align: center;
    font-weight: 700;
    font-size: 40px;
    line-height: 60px;
    color: var(--brand-white);
  }
</style>
</head>
<body>
  <div class="sign-frame">
    <div class="sign">
      <svg class="sign-art" viewBox="0 0 1570 810" xmlns="http://www.w3.org/2000/svg">
        <defs>
          <radialGradient id="pattern-fade" cx="0.1" cy="0.2" r="0.75">
            <stop offset="0" stop-color="#e6e8ea"/>
            <stop offset="1" stop-color="#ffffff" stop-opacity="0"/>
          </radialGradient>
          <linearGradient id="orange-fill" x1="0" y1="0" x2="1" y2="0">
            <stop offset="0" stop-color="#ef8a3c"/>
            <stop offset="0.5" stop-color="#f4a23a"/>
            <stop offset="1" stop-color="#ef8a3c"/>
          </linearGradient>
          <linearGradient id="blue-fill" x1="0" y1="0" x2="0" y2="1">
            <stop offset="0" stop-color="#1a67ad"/>
            <stop offset="1" stop-color="#114f8d"/>
          </linearGradient>
        </defs>
        <rect class="hex-pattern" x="0" y="0" width="700" height="560" fill="url(#pattern-fade)" role="img" aria-label="Faint hexagon pattern decoration"/>
        <path class="services-panel" d="M903,0 H1570 V810 H838 C790,600 760,420 790,260 C810,150 850,60 903,0 Z" fill="url(#blue-fill)"/>
        <path class="services-tab" d="M958,95 H1570 V225 H958 A65,65 0 0 1 958,95 Z" fill="var(--brand-red)"/>
        <path class="web-lens" d="M358,656 Q800,530 1243,645 L1243,790 L358,790 Z" fill="url(#orange-fill)"/>
        <path class="swoosh-red" d="M0,485 C500,800 1100,830 1570,455 V810 H0 Z" fill="var(--brand-red)"/>
        <path class="swoosh-dark" d="M0,590 C500,860 1100,880 1570,550 V810 H0 Z" fill="var(--brand-red-dark)"/>
        <path class="swoosh-white" d="M0,608 C500,878 1100,888 1570,572 V810 H0 Z" fill="var(--brand-white)"/>
        <path class="swoosh-edge" d="M0,485 C500,800 1100,830 1570,455" fill="none" stroke="var(--brand-white)" stroke-width="14"/>
        <path class="corner-blue-left" d="M0,675 C140,720 270,770 393,810 H0 Z" fill="var(--brand-blue)"/>
        <path class="corner-blue-right" d="M1203,810 C1340,770 1470,720 1570,670 V810 Z" fill="var(--brand-blue)"/>
      </svg>

      <h1 class="brand-name">Tidewell</h1>
      <p class="brand-tagline"><span class="tag-electrical">Electrical</span><span class="tag-air">Air Conditioning</span><span class="tag-plumbing">Plumbing</span></p>

      <h2 class="services-title">SERVICES</h2>
      <p class="services-list">Electrical • AC &amp;<br>Plumbing • Installation<br>• Service • Repairs<br>and Maintenance</p>

      <p class="website">www.Tidewell.com</p>
    </div>
  </div>
</body>
</html>
```